Halvorn spray foam and Environmental

I have business cards but need new ones. The ones I have are very bland. Here is. Y company website http://www.halvornsprayfoam.ca

Also I can send you copies of the current cards
I would also need my current logo on the new design as well.. Also spray foam and Environmental

Industry/Entity Type

Business

Logo Text

Halvorn.

```html
<!DOCTYPE html>
<html lang="en">
<head>
<meta charset="utf-8">
<title>Halvorn Business Cards</title>
<link href="https://fonts.googleapis.com/css2?family=Lato:wght@400;700;900&family=EB+Garamond:wght@400&display=swap" rel="stylesheet">
<style>
  :root {
    --stage: #e4e5e7;
    --card: #0a0a0a;
    --purple: #7b4d9c;
    --green: #4cb84a;
    --grey-text: #8d8d8d;
    --white: #f2f2f2;
  }
  * { margin: 0; padding: 0; box-sizing: border-box; }
  html, body { width: 1200px; height: 1200px; overflow: hidden; }
  body { background: var(--stage); font-family: 'Lato', sans-serif; position: relative; }

  .card {
    position: absolute; left: 180px; width: 840px; height: 480px;
    background: var(--card); border-radius: 4px;
    box-shadow: 0 10px 24px rgba(0,0,0,0.25);
  }
  .card--front { top: 90px; }
  .card--back  { top: 630px; }

  .brand { display: flex; align-items: center; gap: 14px; }
  .brand__square { width: 60px; height: 44px; border-radius: 6px; background: var(--purple); flex: none; }
  .brand__name {
    font-family: 'Lato', sans-serif; font-weight: 900; color: var(--purple);
    text-transform: uppercase; line-height: 1; letter-spacing: 0.5px;
  }
  .tagline { font-family: 'EB Garamond', serif; line-height: 1; white-space: nowrap; }

  .card--front .brand-block {
    position: absolute; left: 50%; top: 50%; transform: translate(-50%, -60%);
    display: flex; flex-direction: column; align-items: flex-start; gap: 10px;
  }
  .card--front .brand__name { font-size: 26px; }
  .card--front .tagline { font-size: 30px; color: var(--grey-text); }

  .card--back .brand-block {
    position: absolute; left: 70px; top: 96px;
    display: flex; flex-direction: column; gap: 10px;
  }
  .card--back .brand__name { font-size: 26px; }
  .card--back .tagline { font-size: 32px; color: var(--green); }

  .person { position: absolute; left: 500px; top: 130px; }
  .person__name { font-weight: 900; font-size: 34px; color: var(--green); text-transform: uppercase; letter-spacing: -0.5px; line-height: 1; }
  .person__role { font-size: 17px; color: var(--white); margin-top: 6px; }

  .contact-list { list-style: none; margin-top: 20px; display: flex; flex-direction: column; gap: 10px; }
  .contact-item { display: flex; align-items: center; gap: 10px; font-size: 17px; color: var(--white); }
  .icon { width: 22px; height: 22px; flex: none; }

  .address { position: absolute; left: 70px; top: 370px; display: flex; align-items: center; gap: 12px; color: var(--white); font-size: 18px; line-height: 1.35; }
  .address .icon { width: 26px; height: 26px; }
</style>
</head>
<body>

<section class="card card--front" aria-label="Card front">
  <div class="brand-block">
    <div class="brand">
      <span class="brand__square"></span>
      <span class="brand__name">Halvorn Spray Foam Ltd.</span>
    </div>
    <p class="tagline">Residential &amp; Commercial</p>
  </div>
</section>

<section class="card card--back" aria-label="Card back">
  <div class="brand-block">
    <div class="brand">
      <span class="brand__square"></span>
      <span class="brand__name">Halvorn Environmental</span>
    </div>
    <p class="tagline">Residential &amp; Commercial</p>
  </div>

  <div class="person">
    <h1 class="person__name">Marek Lund</h1>
    <p class="person__role">Director</p>
    <ul class="contact-list">
      <li class="contact-item">
        <svg class="icon" viewBox="0 0 22 22"><rect width="22" height="22" rx="4" fill="#4cb84a"/><path d="M7 5c1 0 2 2.5 1.6 3.2L7.8 9.3c.8 1.7 2.2 3.1 3.9 3.9l1.1-.8c.7-.4 3.2.6 3.2 1.6 0 1.4-1.3 2.5-2.7 2.4C9 16 6 13 5.6 8.7 5.5 6.3 5.6 5 7 5z" fill="#fff"/></svg>
        <span>(604) 555-0182</span>
      </li>
      <li class="contact-item">
        <svg class="icon" viewBox="0 0 22 22"><rect width="22" height="22" rx="4" fill="#4cb84a"/><rect x="5" y="7" width="12" height="8" rx="1" fill="#fff"/><path d="M5 7.5l6 4.5 6-4.5" stroke="#4cb84a" stroke-width="1.2" fill="none"/></svg>
        <span>enviro@halvornmail.ca</span>
      </li>
      <li class="contact-item">
        <svg class="icon" viewBox="0 0 22 22"><rect width="22" height="22" rx="4" fill="#4cb84a"/><g stroke="#fff" stroke-width="1.3" fill="none"><circle cx="11" cy="11" r="6"/><ellipse cx="11" cy="11" rx="2.6" ry="6"/><path d="M5 11h12"/></g></svg>
        <span>www.halvornenvironmental.ca</span>
      </li>
    </ul>
  </div>

  <div class="address">
    <svg class="icon" viewBox="0 0 22 22"><rect width="22" height="22" rx="4" fill="#4cb84a"/><path d="M11 4a5 5 0 0 0-5 5c0 3.6 5 9 5 9s5-5.4 5-9a5 5 0 0 0-5-5z" fill="#fff"/><circle cx="11" cy="9" r="1.8" fill="#4cb84a"/></svg>
    <p>4820 Larchmont Way Burnaby<br>British Columbia V5H 2K9, CA</p>
  </div>
</section>

</body>
</html>
```